IT services web page design

Hello!

We need new design for our web site, obviously :)

Our company is service oriented and we are maintaining, configuring and fixing problems for IT + selling other internet related services.

Our speciality are in area of internet services (web, dns, email, databases, backup...) and internet servers technology.

We also provide service and sales of Zentor Apps and Halvorix Quorvo365 for which we are certified by Zentor and Halvorix.

Other services that we provide (not so in focus) are: VPS hosting, remote backup, web hosting, vexalink fixing...

People mostly call us when they have a problems and this is core idea that new web site has to communicate - We can fix your server / web / email problems, save your money and as* :)

Our team have 15+ years experience with all range of internet technology + bunch of certificates from Halvorix and Tandix [we need to show people we have certificates].
Our qualities: experience, knowledge, delivery on time

In start we will not have blog section, but we need it in future. We also need place for plonkit feeds on web site.

Depth of the site should be max. level 2.

This site will go out in two languages so we need switch button on page from pone language to another.

Target Market(s)

small and mid size business that use internet services for daily operations and main business

Industry/Entity Type

Internet

Requirements
Must have
• * design should be in the way that responsive web could be made

Nice to have
• Long format will be OK for us. Like today pages that list all services and benefits on one loooong web page...

Logo is in attachment. It will be nice to have it on web site but if you find it not appropriate you can change it or put another one.

```html
<!DOCTYPE html>
<html lang="en">
<head>
<meta charset="utf-8">
<title>Corvane Group – IT Services</title>
<link rel="stylesheet" href="https://fonts.googleapis.com/css2?family=Roboto:wght@300;400;700&family=Roboto+Condensed:wght@300;400;700&display=swap">
<style>
:root{
  --ink:#333;
  --muted:#555;
  --blue:#1e6ea8;
  --blue-dark:#135485;
  --blue-light:#3a9ad9;
  --black:#111;
  --bar:#1a1a1a;
  --gray-band:#ececec;
  --card-border:#d5d5d5;
  --footer:#4d7c9c;
  --footer-dark:#2f5a78;
  --white:#fff;
  --link:#9fd3ff;
}
*{box-sizing:border-box;margin:0;padding:0}
html,body{width:1200px;height:3400px;overflow:hidden}
body{position:relative;background:var(--white);font-family:"Roboto",Arial,sans-serif;color:var(--ink)}
.abs{position:absolute}

/* top bar */
.topbar{left:0;top:0;width:1200px;height:58px;background:var(--black)}
.brand{left:30px;top:12px;font:700 30px/34px "Roboto",sans-serif;color:var(--white);letter-spacing:3px;text-transform:uppercase}
.topbar-links{right:40px;top:0;height:58px;display:flex;align-items:center;gap:22px;font-size:13px;color:var(--white)}
.topbar-links .sep{opacity:.6}
.lang{background:var(--white);color:var(--ink);padding:3px 8px;width:96px;display:flex;justify-content:space-between;font-size:13px}

/* header */
.header{left:0;top:58px;width:1200px;height:100px}
.phone{left:30px;top:30px;display:flex;align-items:center;gap:12px;font-size:20px;color:var(--ink)}
.nav{left:390px;top:22px;width:780px;display:flex;justify-content:space-between;font:400 15px "Roboto",sans-serif;color:#666;text-transform:uppercase}
.nav a{padding:10px 16px;color:inherit;text-decoration:none}
.nav .active{color:var(--blue);border-top:1px solid var(--blue-light);border-bottom:1px solid var(--blue-light)}

/* hero */
.hero{left:30px;top:162px;width:1138px;height:668px;background:linear-gradient(100deg,#0d3d66 0%,#4c8ec0 35%,#9bc6e2 55%,#5d7a90 80%,#2f3d4a 100%);border-bottom:6px solid #0a2c4a}
.hero-circle{left:70px;top:220px;width:560px;height:560px;border-radius:50%;background:rgba(255,255,255,.55)}
.hero-copy{left:90px;top:390px;width:420px;text-align:center}
.hero-kicker{font:400 22px "Roboto Condensed",sans-serif;color:var(--blue-dark);text-transform:uppercase}
.hero-title{margin-top:16px;font:700 32px/38px "Roboto Condensed",sans-serif;color:var(--blue-dark);text-transform:uppercase}
.hero-text{margin-top:20px;font:400 22px/30px "Roboto",sans-serif;color:var(--black)}
.dots{left:550px;top:790px;display:flex;gap:12px}
.dots span{width:20px;height:20px;border-radius:50%;background:#b5c3cc;border:2px solid #fff}
.dots .on{background:var(--blue-light)}

/* section headings */
.section-title{left:0;width:1200px;text-align:center;font:300 36px "Roboto",sans-serif;text-transform:uppercase}
.lead{left:30px;width:1140px;text-align:center;font:400 14px/24px "Roboto",sans-serif;color:var(--muted)}

/* services */
.services-band{left:0;top:1108px;width:1200px;height:600px;background:linear-gradient(#f6f6f6,var(--gray-band) 40%,#f3f3f3)}
.services-band::before{content:"";position:absolute;left:588px;top:-1px;border:12px solid transparent;border-top-color:#fff}
.cards{left:30px;top:1265px;width:1140px;display:flex;justify-content:space-between}
.card{width:150px;height:230px;background:var(--white);border:2px solid var(--card-border);display:flex;flex-direction:column;align-items:center;padding-top:24px;position:relative}
.card .ring{width:110px;height:110px;border-radius:50%;border:4px solid var(--blue);display:flex;align-items:center;justify-content:center}
.card .label{margin-top:14px;text-align:center;font:400 17px/20px "Roboto",sans-serif;color:#444}
.card.active{background:var(--blue);border-color:var(--blue-dark)}
.card.active .ring{border-color:var(--white)}
.card.active .label{color:var(--white)}
.card.active::after{content:"";position:absolute;left:55px;bottom:-22px;border:18px solid transparent;border-top-color:var(--blue)}
.service-list{left:30px;top:1523px;width:440px;font:400 15px/24px "Roboto",sans-serif;color:var(--muted)}

/* testimonials */
.arrow{top:1878px;width:66px;height:66px;border-radius:50%;background:#e7e7e7;display:flex;align-items:center;justify-content:center}
.avatar{left:550px;top:1845px;width:110px;height:110px;border-radius:50%;background:linear-gradient(#c9d3da,#8a6b55);border:4px solid #ddd}
.client{left:0;top:1992px;width:1200px;text-align:center;font:400 15px "Roboto",sans-serif;color:var(--ink)}
.client em{font-style:italic}

/* team */
.team{left:0;top:2193px;width:1200px;height:635px;background:linear-gradient(90deg,#e9e4df,#cfc6bd 40%,#dcd6cf 70%,#bfb5ab)}
.team-copy{left:140px;top:2350px;width:470px;text-align:center}
.team-we{font:300 48px "Roboto",sans-serif;color:var(--black)}
.team-sub{font:300 36px "Roboto",sans-serif;color:var(--blue);text-transform:uppercase;margin-top:4px}
.team-text{margin-top:18px;font:400 20px/30px "Roboto",sans-serif;color:var(--black)}
.btn{left:197px;top:2617px;width:283px;height:63px;background:linear-gradient(var(--blue),var(--blue-dark));color:var(--white);display:flex;align-items:center;justify-content:center;font:700 26px "Roboto Condensed",sans-serif;text-transform:uppercase}
.device-photo{left:660px;top:2200px;width:380px;height:628px;background:linear-gradient(#f2f2f2,#dcdcdc 70%,#c9b3a4)}
.why-panel{left:696px;top:2268px;width:250px;height:420px;background:#d9d9d9}
.why-title{background:#bfbfbf;text-align:center;font:700 20px/46px "Roboto Condensed",sans-serif;color:#222;text-transform:uppercase}
.why-list{list-style:none;padding:14px 12px 0}
.why-list li{display:flex;align-items:center;gap:8px;height:54px;font:400 13px "Roboto",sans-serif;color:#222;white-space:nowrap}
.tick{flex:none;width:24px;height:24px;background:#fff;border:2px solid #7a9a3a;display:flex;align-items:center;justify-content:center}

/* footer */
.footer{left:0;top:2828px;width:1200px;height:506px;background:linear-gradient(var(--footer),var(--footer-dark))}
.fcol{top:2870px;color:var(--white)}
.fcol h4{font:400 17px "Roboto Condensed",sans-serif;text-transform:uppercase;margin-bottom:34px}
.quick li{list-style:none;font-size:14px;line-height:22px}
.feed{display:flex;gap:14px;margin-bottom:30px}
.feed .bird{flex:none;width:32px;height:32px;border-radius:50%;background:var(--white)}
.feed p,.post p{font-size:13px;line-height:17px;width:200px}
.feed .from{font-size:14px;margin-bottom:14px}
.posted{margin-top:10px;font-size:13px;font-style:italic}
.posted span,.readmore{color:var(--link)}
.post h5{font:700 14px "Roboto",sans-serif;margin-bottom:12px}
.post{margin-bottom:30px}
.readmore{font-size:13px;margin-top:6px}
.contact p{font-size:14px;line-height:22px}
.contact .gap{margin-top:34px}
.follow{margin-top:30px;font:400 17px "Roboto Condensed",sans-serif;text-transform:uppercase}
.socials{margin-top:16px;display:grid;grid-template-columns:repeat(2,auto);gap:10px 18px;justify-content:start}
.socials li{list-style:none;display:flex;align-items:center;gap:8px;font-size:14px}
.socials i{width:22px;height:22px;border-radius:50%;background:var(--white)}
.bottombar{left:0;top:3334px;width:1200px;height:66px;background:var(--bar);color:#ddd;text-align:center;font:400 17px/66px "Roboto",sans-serif}
</style>
</head>
<body>

<header>
  <div class="abs topbar">
    <div class="abs brand">Corvane Group</div>
    <div class="abs topbar-links">
      <span>Help Desk</span>
      <span>Login</span><span class="sep">|</span><span>Register</span>
      <span class="lang">English <span>&#9662;</span></span>
    </div>
  </div>
  <div class="abs header">
    <div class="abs phone">
      <svg width="34" height="28" viewBox="0 0 34 28"><path d="M3 8c0-4 6-6 14-6s14 2 14 6v3h-7V8H10v3H3z" fill="#1e6ea8"/><rect x="6" y="13" width="22" height="13" rx="2" fill="#1e6ea8"/><circle cx="17" cy="19.5" r="3.5" fill="#fff"/></svg>
      <span>000-000-0000</span>
    </div>
    <nav class="abs nav">
      <a class="active">Home</a><a>About Us</a><a>Services</a><a>Partners</a><a>Blog</a><a>Contact Us</a>
    </nav>
  </div>
</header>

<section>
  <div class="abs hero" role="img" aria-label="Photo of a businessman touching a glowing network of technology icons"></div>
  <div class="abs hero-circle"></div>
  <div class="abs hero-copy">
    <div class="hero-kicker">Corvane Group</div>
    <div class="hero-title">Provid the best IT and<br>internet services</div>
    <div class="hero-text">We are Spelist in Maintaining ,<br>configuring and Fixing the It and<br>Internet services</div>
  </div>
  <div class="abs dots"><span class="on"></span><span></span><span class="on"></span></div>
</section>

<section>
  <h2 class="abs section-title" style="top:852px;color:var(--blue-light)">About Corvane</h2>
  <p class="abs lead" style="top:912px">Lorem Ipsum is simply dummy text of the printing and typesetting industry. Lorem Ipsum has been the industry's standard dummy text ever since the 1500s, when an unknown printer took a galley of type and scrambled it to make a type specimen book. It has survived not only five centuries, but also the leap into electronic typesetting, remaining essentially unchanged. It was popularised in the 1960s with the release of Letraset sheets containing Lorem Ipsum passages, and more recently with desktop publishing software like Aldus PageMaker including versions of Lorem Ipsum.</p>
</section>

<section>
  <div class="abs services-band"></div>
  <h2 class="abs section-title" style="top:1168px;color:#444;font-size:32px">Services We Provide</h2>
  <div class="abs cards">
    <div class="card active">
      <div class="ring"><svg width="54" height="50" viewBox="0 0 54 50"><rect x="2" y="2" width="50" height="34" rx="3" fill="#fff"/><rect x="22" y="36" width="10" height="8" fill="#fff"/><rect x="14" y="44" width="26" height="4" fill="#fff"/></svg></div>
      <div class="label">Web<br>Services</div>
    </div>
    <div class="card">
      <div class="ring"><svg width="52" height="52" viewBox="0 0 52 52" fill="none"><circle cx="26" cy="26" r="22" fill="#1e6ea8"/><g stroke="#fff" stroke-width="2"><ellipse cx="26" cy="26" rx="9" ry="22"/><path d="M4 26h44M8 14h36M8 38h36M26 4v44"/></g></svg></div>
      <div class="label">DNS<br>Services</div>
    </div>
    <div class="card">
      <div class="ring"><svg width="56" height="46" viewBox="0 0 56 46"><path d="M2 6h18l5 5h29v33H2z" fill="#1e6ea8"/></svg></div>
      <div class="label">Database<br>Services</div>
    </div>
    <div class="card">
      <div class="ring"><svg width="56" height="40" viewBox="0 0 56 40"><rect x="2" y="2" width="52" height="36" rx="4" fill="#1e6ea8"/><rect x="10" y="9" width="36" height="14" rx="2" fill="#fff"/><circle cx="19" cy="16" r="4" fill="#1e6ea8"/><circle cx="37" cy="16" r="4" fill="#1e6ea8"/></svg></div>
      <div class="label">Back up<br>Services</div>
    </div>
    <div class="card">
      <div class="ring"><svg width="34" height="56" viewBox="0 0 34 56"><rect x="2" y="2" width="30" height="52" rx="5" fill="#1e6ea8"/><rect x="6" y="9" width="22" height="34" fill="#fff"/><circle cx="17" cy="48" r="3" fill="#fff"/></svg></div>
      <div class="label">Application<br>Services</div>
    </div>
    <div class="card">
      <div class="ring"><svg width="40" height="56" viewBox="0 0 40 56"><rect x="2" y="2" width="36" height="52" rx="3" fill="#1e6ea8"/><g fill="#fff"><rect x="7" y="9" width="26" height="6"/><rect x="7" y="20" width="26" height="6"/><rect x="7" y="31" width="26" height="6"/><rect x="7" y="42" width="26" height="6"/></g></svg></div>
      <div class="label">Web<br>Hosting</div>
    </div>
  </div>
  <p class="abs service-list">Website Design, Website Redesign, Website Maintenance, Flash Web Design, Custom Web Design, Web 2.0 Development, Custom Web Development, E-commerce Web Development, Content Management Syste</p>
</section>

<section>
  <h2 class="abs section-title" style="top:1755px;color:var(--blue-light);text-transform:none">What Our Clients Say About US</h2>
  <div class="abs arrow" style="left:45px"><svg width="20" height="26" viewBox="0 0 20 26"><path d="M16 2 4 13l12 11" stroke="#111" stroke-width="5" fill="none"/></svg></div>
  <div class="abs arrow" style="left:1085px"><svg width="20" height="26" viewBox="0 0 20 26"><path d="M4 2l12 11L4 24" stroke="#111" stroke-width="5" fill="none"/></svg></div>
  <div class="abs avatar" role="img" aria-label="Client portrait"></div>
  <p class="abs client"><em>Maren Okoli</em> &nbsp;( ashgroveleaf.net )</p>
  <p class="abs lead" style="top:2030px">Lorem Ipsum is simply dummy text of the printing and typesetting industry. Lorem Ipsum has been the industry's standard dummy text ever since the 1500s, when an unknown printer took a galley of type and scrambled it to make a type specimen book. It has survived not only five centuries, but also the leap into electronic typesetting, remaining essentially unchanged. It was popularised in the 1960s with the release of Letraset sheets containing Lorem Ipsum passages, and more recently with desktop publishing software like Aldus PageMaker including versions of Lorem Ipsum.</p>
</section>

<section>
  <div class="abs team" role="img" aria-label="Mosaic of team member portrait photos"></div>
  <div class="abs team-copy">
    <div class="team-we">WE ARE</div>
    <div class="team-sub">Team of Expert</div>
    <p class="team-text">Team of Hard Worker have 15+ year experience with all range of internet Technology + Bunch of Certificate from halvorix and Tandix.</p>
  </div>
  <div class="abs btn">Contact Us Now</div>
  <div class="abs device-photo" role="img" aria-label="Photo of a hand holding a white tablet"></div>
  <div class="abs why-panel">
    <div class="why-title">Whys Us</div>
    <ul class="why-list">
      <li><span class="tick"><svg width="16" height="14" viewBox="0 0 16 14"><path d="M1 7l5 5 9-11" stroke="#6a9a1a" stroke-width="3" fill="none"/></svg></span>Lorem Ipsum is simply dummy</li>
      <li><span class="tick"><svg width="16" height="14" viewBox="0 0 16 14"><path d="M1 7l5 5 9-11" stroke="#6a9a1a" stroke-width="3" fill="none"/></svg></span>Lorem Ipsum is simply dummy</li>
      <li><span class="tick"><svg width="16" height="14" viewBox="0 0 16 14"><path d="M1 7l5 5 9-11" stroke="#6a9a1a" stroke-width="3" fill="none"/></svg></span>Lorem Ipsum is simply dummy</li>
      <li><span class="tick"><svg width="16" height="14" viewBox="0 0 16 14"><path d="M1 7l5 5 9-11" stroke="#6a9a1a" stroke-width="3" fill="none"/></svg></span>Lorem Ipsum is simply dummy</li>
      <li><span class="tick"><svg width="16" height="14" viewBox="0 0 16 14"><path d="M1 7l5 5 9-11" stroke="#6a9a1a" stroke-width="3" fill="none"/></svg></span>Lorem Ipsum is simply dummy</li>
      <li><span class="tick"><svg width="16" height="14" viewBox="0 0 16 14"><path d="M1 7l5 5 9-11" stroke="#6a9a1a" stroke-width="3" fill="none"/></svg></span>Lorem Ipsum is simply dummy</li>
    </ul>
  </div>
</section>

<footer>
  <div class="abs footer"></div>
  <div class="abs fcol quick" style="left:30px">
    <h4>Quick Links</h4>
    <ul><li>Home</li><li>About us</li><li>Sagome</li><li>Services</li><li>Clients</li><li>Privacy policy</li><li>Terms of use</li><li>Contact us</li></ul>
  </div>
  <div class="abs fcol" style="left:332px">
    <h4>Plonkit Feeds</h4>
    <div class="feed"><span class="bird"></span><div><p class="from">info@corvane.net</p><p>Lorem Ipsum is simply dummy text of the printing and typesetting industry. Lorem Ipsum has been the industry's standard</p><p class="posted">Posted : <span>14 Hours Ago</span></p></div></div>
    <div class="feed"><span class="bird"></span><div><p class="from">info@corvane.net</p><p>Lorem Ipsum is simply dummy text of the printing and typesetting industry. Lorem Ipsum has been the industry's standard</p><p class="posted">Posted : <span>14 Hours Ago</span></p></div></div>
  </div>
  <div class="abs fcol" style="left:629px">
    <h4>Blog</h4>
    <div class="post"><h5>Blog Headline Goes Here</h5><p>Lorem Ipsum is simply dummy text of the printing and typesetting industry. Lorem Ipsum has been the industry's standard dummy text ever since the 1500s, when an</p><p class="readmore">Read more</p></div>
    <div class="post"><h5>Blog Headline Goes Here</h5><p>Lorem Ipsum is simply dummy text of the printing and typesetting industry. Lorem Ipsum has been the industry's standard dummy text ever since the 1500s, when an</p><p class="readmore">Read more</p></div>
  </div>
  <div class="abs fcol contact" style="left:926px">
    <h4>Contact Us</h4>
    <p>418 Harlow Ridge Rd<br>Brenton Falls, Ohio<br>40117, USA</p>
    <p class="gap">CALL US : <span style="color:var(--link)">555 014 2290</span><br>EMAIL : <span style="color:var(--link)">help@corvane.net</span></p>
    <div class="follow">Follow Us :</div>
    <ul class="socials"><li><i></i>Netlane</li><li><i></i>Vidora</li><li><i></i>Palsy</li><li><i></i>Plonkit</li></ul>
  </div>
  <div class="abs bottombar">© 2013 CorvaneGroup, Inc. All rights reserved.</div>
</footer>

</body>
</html>
```